Maplewood Youth Relief Trust

I need a site for a not for profit organization. The site requires an about us page, current projects, get involved and a contact us page
our not for profit will focus on three projects at a time the three focus would be childrens cancer, sick children and disadvantaged children
our logo is red and white so something that will complement this color scheme

Coding

Coded - Design and coding required

Number of Pages Required

5+ page

Font styles to use
Sans Serif

Colors
ec1f27
33a6d7
fbed22

Requirements
Must have
• an about us, contact us, current projects, home page, and
• get involved pages
• ability to update our pages easily

```html
<!DOCTYPE html>
<html lang="en">
<head>
<meta charset="utf-8">
<title>Contact Us – Maplewood Youth Relief Trust</title>
<link rel="stylesheet" href="https://fonts.googleapis.com/css2?family=Open+Sans:wght@400;600&family=Figtree:wght@400;600&display=swap">
<style>
  :root {
    --brand-red: #ec1f27;
    --brand-blue: #33a6d7;
    --brand-yellow: #fbed22;
    --text-grey: #5f5f5f;
    --nav-grey: #595959;
    --white: #ffffff;
    --button-orange: #f5701f;
    --placeholder: #8a8a8a;
  }
  * { box-sizing: border-box; margin: 0; padding: 0; }
  html, body {
    width: 1200px;
    height: 590px;
    overflow: hidden;
    background: var(--white);
  }
  body {
    position: relative;
    font-family: "Open Sans", sans-serif;
  }
  .site-header {
    position: absolute;
    left: 0; top: 0;
    width: 1200px; height: 81px;
    background: var(--white);
  }
  .brand-name {
    position: absolute;
    left: 51px; top: 21px;
    font-family: "Open Sans", sans-serif;
    font-weight: 600;
    font-size: 27px;
    letter-spacing: -0.5px;
    color: var(--brand-red);
    white-space: nowrap;
  }
  .main-nav a {
    position: absolute;
    top: 0;
    height: 81px;
    line-height: 81px;
    font-size: 14px;
    font-weight: 600;
    color: var(--nav-grey);
    text-decoration: none;
    text-transform: uppercase;
    white-space: nowrap;
  }
  .main-nav .nav-home { left: 532px; }
  .main-nav .nav-about { left: 626px; }
  .main-nav .nav-projects { left: 737px; }
  .main-nav .nav-involved { left: 911px; }
  .main-nav .nav-contact {
    left: 1037px;
    width: 112px;
    text-align: center;
    background: var(--brand-red);
    color: var(--white);
  }
  .hero-band {
    position: absolute;
    left: 0; top: 81px;
    width: 1200px; height: 49px;
    background: linear-gradient(90deg, #e9dccb 0%, #d9bfa3 30%, #efe3d3 50%, #d6b89a 75%, #eadbc8 100%);
  }
  .contact-section {
    position: absolute;
    left: 51px; top: 170px;
  }
  .contact-title {
    font-family: "Figtree", sans-serif;
    font-weight: 400;
    font-size: 27px;
    color: var(--brand-red);
    line-height: 36px;
  }
  .contact-details {
    margin-top: 7px;
    font-size: 21px;
    line-height: 33px;
    color: var(--text-grey);
  }
  .site-footer {
    position: absolute;
    left: 0; top: 375px;
    width: 1200px; height: 215px;
    background: var(--brand-red);
    color: var(--white);
  }
  .footer-column { position: absolute; top: 29px; }
  .footer-heading {
    font-family: "Figtree", sans-serif;
    font-weight: 600;
    font-size: 18px;
    line-height: 24px;
    letter-spacing: 0.3px;
    margin-bottom: 19px;
  }
  .col-address { left: 128px; width: 260px; }
  .col-company { left: 414px; }
  .col-newsletter { left: 583px; width: 280px; }
  .col-connect { left: 897px; }
  .address-text {
    font-size: 16px;
    line-height: 25px;
  }
  .footer-links { list-style: none; }
  .footer-links li {
    font-size: 16px;
    line-height: 30px;
    margin-left: 2px;
  }
  .footer-links li:first-child { margin-top: -4px; }
  .newsletter-text {
    font-size: 13px;
    line-height: 18px;
    margin-left: 1px;
  }
  .newsletter-form {
    position: absolute;
    left: 1px; top: 128px;
    width: 269px; height: 32px;
    background: var(--white);
  }
  .newsletter-input {
    position: absolute;
    left: 9px; top: 0;
    line-height: 32px;
    font-size: 13px;
    color: var(--placeholder);
  }
  .newsletter-button {
    position: absolute;
    right: 5px; top: 4px;
    width: 69px; height: 24px;
    background: var(--button-orange);
    color: var(--white);
    font-size: 13px;
    line-height: 24px;
    text-align: center;
    border-radius: 2px;
    text-transform: uppercase;
  }
  .social-row {
    display: flex;
    gap: 9px;
    margin-left: -4px;
    margin-top: -6px;
  }
  .social-dot {
    width: 37px; height: 37px;
    border-radius: 50%;
    background: var(--white);
  }
  .copyright {
    margin-top: 17px;
    font-size: 11px;
    line-height: 15px;
  }
</style>
</head>
<body>
  <header class="site-header">
    <div class="brand-name">Maplewood Youth Relief Trust</div>
    <nav class="main-nav">
      <a class="nav-home" href="#">Home</a>
      <a class="nav-about" href="#">About Us</a>
      <a class="nav-projects" href="#">Current Projects</a>
      <a class="nav-involved" href="#">Get Involved</a>
      <a class="nav-contact" href="#">Contact Us</a>
    </nav>
  </header>

  <div class="hero-band" role="img" aria-label="Photograph of smiling children resting their heads together"></div>

  <main class="contact-section">
    <h1 class="contact-title">Contact Us</h1>
    <p class="contact-details">Address 27 Birchfield Lane, Kingsbridge, Ontario L4R 8T2<br>Phone number 1 855 010-4732</p>
  </main>

  <footer class="site-footer">
    <div class="footer-column col-address">
      <h2 class="footer-heading">Our Address</h2>
      <p class="address-text">GivingKit is a library of<br>Crowdfunding and Charity<br>with predefined elements which<br>helps you to build your own site.</p>
    </div>
    <div class="footer-column col-company">
      <h2 class="footer-heading">Compay</h2>
      <ul class="footer-links">
        <li>About Us</li>
        <li>Current Projects</li>
        <li>Get Involved</li>
        <li>Contact Us</li>
      </ul>
    </div>
    <div class="footer-column col-newsletter">
      <h2 class="footer-heading">Sign up for newsletter</h2>
      <p class="newsletter-text">Claritas est etiam processus dynamicus, qui<br>sequitur mutationem consuetudium lectorum.</p>
      <div class="newsletter-form">
        <span class="newsletter-input">Enter Your Email...</span>
        <span class="newsletter-button">Sign Up</span>
      </div>
    </div>
    <div class="footer-column col-connect">
      <h2 class="footer-heading">Connect with Us</h2>
      <div class="social-row">
        <span class="social-dot"></span>
        <span class="social-dot"></span>
        <span class="social-dot"></span>
        <span class="social-dot"></span>
      </div>
      <p class="copyright">© 2016&nbsp; Maplewood Youth Relief</p>
    </div>
  </footer>
</body>
</html>
```